Company Eco-System 1 Page Graphic

We need a 1 page visual of what our company does and all of the different parts of the company and what they do.
We would like it to be as simple as possible, modern, clean.
Our logo and colour palette are attached.
We are an events management company and we want to show our shareholders a graphic that demonstrates how the different parts of our company work together to deliver events and our strategic goals

Target Market(s)

Our local Council which we are owned by

Industry/Entity Type

Events Management

Font styles to use
Other font styles liked:
• Calibri light

```html
<!DOCTYPE html>
<html lang="en">
<head>
<meta charset="utf-8">
<title>Events Eco-System</title>
<link rel="stylesheet" href="https://fonts.googleapis.com/css2?family=Oswald:wght@400;500&family=Montserrat:wght@700;800&display=swap">
<style>
  :root {
    --ink: #111111;
    --paper: #ffffff;
    --tone-dark: #383838;
    --tone-mid: #6b6b6b;
    --tone-light: #a3a3a3;
    --tone-pale: #c2c2c2;
    --link: #1c1c1c;
    --accent: #e0412b;
  }
  html, body { margin: 0; padding: 0; width: 1200px; height: 1200px; overflow: hidden; background: var(--paper); }
  .ecosystem { display: block; width: 1200px; height: 1200px; }
  .boundary { fill: none; stroke: var(--ink); stroke-width: 1.3; stroke-dasharray: 6 5; }
  .goal-halo, .goal-label { font-family: 'Montserrat', sans-serif; font-weight: 700; font-size: 24px; letter-spacing: 0.5px; dominant-baseline: middle; }
  .goal-halo { fill: var(--paper); stroke: var(--paper); stroke-width: 16px; stroke-linejoin: round; }
  .goal-label { fill: var(--ink); }
  .icon { fill: none; stroke: var(--ink); stroke-width: 2.4; stroke-linecap: round; stroke-linejoin: round; }
  .spoke { stroke: var(--link); stroke-width: 1.8; }
  .branch { stroke: var(--link); stroke-width: 1.4; }
  .tone-dark { fill: var(--tone-dark); }
  .tone-mid { fill: var(--tone-mid); }
  .tone-light { fill: var(--tone-light); }
  .tone-pale { fill: var(--tone-pale); }
  .leaf-label { font-family: 'Oswald', sans-serif; font-size: 9.5px; fill: var(--paper); text-anchor: middle; }
  .hub-disc { fill: var(--ink); }
  .hub-ring { fill: none; stroke: var(--paper); stroke-width: 1.4; }
  .hub-label { font-family: 'Oswald', sans-serif; font-size: 12.5px; fill: var(--paper); text-anchor: middle; }
  .core-outer { fill: var(--paper); stroke: var(--ink); stroke-width: 3; }
  .core-inner { fill: var(--paper); stroke: var(--ink); stroke-width: 1.4; }
  .core-title { font-family: 'Montserrat', sans-serif; font-weight: 800; font-size: 38px; fill: var(--ink); text-anchor: middle; }
  .core-cell { font-family: 'Oswald', sans-serif; font-size: 14px; fill: var(--ink); text-anchor: middle; }
  .core-rule { stroke: var(--ink); stroke-width: 1.2; }
  .phase { font-family: 'Montserrat', sans-serif; font-weight: 700; font-size: 20px; fill: var(--ink); dominant-baseline: middle; text-anchor: middle; }
  .phase-arrow { font-family: 'Montserrat', sans-serif; font-weight: 800; font-size: 14px; fill: var(--accent); dominant-baseline: middle; text-anchor: middle; }
  .brand-name { font-family: 'Montserrat', sans-serif; font-weight: 700; font-size: 36px; letter-spacing: 4px; fill: var(--ink); text-anchor: middle; }
</style>
</head>
<body>
<svg class="ecosystem" viewBox="0 0 1500 1500" xmlns="http://www.w3.org/2000/svg">
  <defs>
    <path id="ring-cw" d="M176,715 A577,577 0 1 1 1330,715 A577,577 0 1 1 176,715"/>
    <path id="ring-ccw" d="M176,715 A577,577 0 1 0 1330,715 A577,577 0 1 0 176,715"/>
    <path id="core-cw" d="M649,730 A111,111 0 1 1 871,730 A111,111 0 1 1 649,730"/>
    <path id="core-ccw" d="M649,730 A111,111 0 1 0 871,730 A111,111 0 1 0 649,730"/>
  </defs>

  <!-- strategic goals boundary -->
  <circle class="boundary" cx="753" cy="715" r="577"/>
  <g class="goal-halos">
    <text class="goal-halo"><textPath href="#ring-cw" startOffset="10.3%" text-anchor="middle">CELEBRATE AND SOURCE LOCAL</textPath></text>
    <text class="goal-halo"><textPath href="#ring-cw" startOffset="38.6%" text-anchor="middle">STRATEGIC PARTNERSHIPS</textPath></text>
    <text class="goal-halo"><textPath href="#ring-ccw" startOffset="7.4%" text-anchor="middle">HEALTH AND SAFETY WELL BEING</textPath></text>
    <text class="goal-halo"><textPath href="#ring-ccw" startOffset="24.6%" text-anchor="middle">ENVIRONMENTAL AND SOCIAL SUSTAINABILITY</textPath></text>
    <text class="goal-halo"><textPath href="#ring-ccw" startOffset="41.4%" text-anchor="middle">STAKEHOLDER ENGAGEMENT</textPath></text>
  </g>
  <g class="goal-labels">
    <text class="goal-label"><textPath href="#ring-cw" startOffset="10.3%" text-anchor="middle">CELEBRATE AND SOURCE LOCAL</textPath></text>
    <text class="goal-label"><textPath href="#ring-cw" startOffset="38.6%" text-anchor="middle">STRATEGIC PARTNERSHIPS</textPath></text>
    <text class="goal-label"><textPath href="#ring-ccw" startOffset="7.4%" text-anchor="middle">HEALTH AND SAFETY WELL BEING</textPath></text>
    <text class="goal-label"><textPath href="#ring-ccw" startOffset="24.6%" text-anchor="middle">ENVIRONMENTAL AND SOCIAL SUSTAINABILITY</textPath></text>
    <text class="goal-label"><textPath href="#ring-ccw" startOffset="41.4%" text-anchor="middle">STAKEHOLDER ENGAGEMENT</textPath></text>
  </g>

  <!-- goal icons -->
  <g class="icon icon-local">
    <circle cx="228" cy="308" r="27"/>
    <ellipse cx="228" cy="308" rx="12" ry="27"/>
    <line x1="201" y1="308" x2="255" y2="308"/>
    <path d="M205,294 H251 M205,322 H251"/>
    <path d="M244,338 C236,328 236,322 236,320 A8,8 0 0 1 252,320 C252,322 252,328 244,338 Z" fill="#fff"/>
    <circle cx="244" cy="320" r="2.5"/>
  </g>
  <g class="icon icon-partnership">
    <path d="M1214,280 L1226,274 L1246,282 L1262,276 L1284,274 L1292,296 L1280,300"/>
    <path d="M1214,280 L1222,302 L1232,302 L1246,314 A4,4 0 0 0 1252,308 L1258,314 A4,4 0 0 0 1264,308 L1270,312 A4,4 0 0 0 1276,304 L1280,300 L1262,284 L1250,292 A5,5 0 0 1 1242,286 L1250,280"/>
  </g>
  <g class="icon icon-safety">
    <path d="M193,1025 L218,1034 L218,1056 C218,1068 207,1077 193,1082 C179,1077 168,1068 168,1056 L168,1034 Z"/>
    <path d="M181,1052 L190,1061 L205,1045"/>
  </g>
  <g class="icon icon-stakeholder">
    <circle cx="1297" cy="1072" r="28"/>
    <circle cx="1297" cy="1044" r="4.5" fill="#fff"/>
    <circle cx="1269" cy="1072" r="4.5" fill="#fff"/>
    <circle cx="1325" cy="1072" r="4.5" fill="#fff"/>
    <circle cx="1297" cy="1100" r="4.5" fill="#fff"/>
    <circle cx="1297" cy="1062" r="7"/>
    <path d="M1284,1088 C1284,1076 1310,1076 1310,1088"/>
  </g>
  <g class="icon icon-sustainability">
    <path d="M724,1362 A34,34 0 0 1 780,1356"/>
    <path d="M780,1392 A34,34 0 0 1 724,1398"/>
    <path d="M776,1348 L781,1357 L772,1359"/>
    <path d="M728,1406 L723,1397 L732,1395"/>
    <path d="M752,1350 C770,1362 770,1392 752,1404 C734,1392 734,1362 752,1350 Z"/>
    <path d="M752,1356 V1404 M752,1372 L762,1364 M752,1372 L742,1364 M752,1386 L762,1378 M752,1386 L742,1378"/>
  </g>

  <!-- spokes from hubs to core -->
  <g class="spokes">
    <line class="spoke" x1="759" y1="355" x2="760" y2="730"/>
    <line class="spoke" x1="968" y1="453" x2="760" y2="730"/>
    <line class="spoke" x1="509" y1="470" x2="760" y2="730"/>
    <line class="spoke" x1="386" y1="650" x2="760" y2="730"/>
    <line class="spoke" x1="1125" y1="637" x2="760" y2="730"/>
    <line class="spoke" x1="435" y1="922" x2="760" y2="730"/>
    <line class="spoke" x1="758" y1="1017" x2="760" y2="730"/>
    <line class="spoke" x1="1041" y1="893" x2="760" y2="730"/>
  </g>

  <!-- branches -->
  <g class="branches">
    <line class="branch" x1="759" y1="355" x2="760" y2="230"/>
    <line class="branch" x1="759" y1="355" x2="681" y2="268"/>
    <line class="branch" x1="759" y1="355" x2="838" y2="267"/>
    <line class="branch" x1="759" y1="355" x2="609" y2="324"/>
    <line class="branch" x1="759" y1="355" x2="848" y2="330"/>
    <line class="branch" x1="759" y1="355" x2="676" y2="453"/>

    <line class="branch" x1="968" y1="453" x2="974" y2="330"/>
    <line class="branch" x1="968" y1="453" x2="1054" y2="353"/>
    <line class="branch" x1="968" y1="453" x2="911" y2="384"/>
    <line class="branch" x1="968" y1="453" x2="849" y2="415"/>
    <line class="branch" x1="968" y1="453" x2="1072" y2="414"/>
    <line class="branch" x1="968" y1="453" x2="848" y2="465"/>
    <line class="branch" x1="968" y1="453" x2="1047" y2="490"/>
    <line class="branch" x1="968" y1="453" x2="852" y2="530"/>

    <line class="branch" x1="509" y1="470" x2="498" y2="359"/>
    <line class="branch" x1="509" y1="470" x2="411" y2="403"/>
    <line class="branch" x1="509" y1="470" x2="582" y2="418"/>
    <line class="branch" x1="509" y1="470" x2="407" y2="491"/>
    <line class="branch" x1="509" y1="470" x2="516" y2="579"/>

    <line class="branch" x1="386" y1="650" x2="316" y2="581"/>
    <line class="branch" x1="386" y1="650" x2="427" y2="574"/>
    <line class="branch" x1="386" y1="650" x2="296" y2="708"/>
    <line class="branch" x1="386" y1="650" x2="451" y2="718"/>

    <line class="branch" x1="1125" y1="637" x2="1064" y2="565"/>
    <line class="branch" x1="1125" y1="637" x2="1202" y2="490"/>
    <line class="branch" x1="1125" y1="637" x2="1221" y2="563"/>
    <line class="branch" x1="1125" y1="637" x2="1008" y2="605"/>
    <line class="branch" x1="1125" y1="637" x2="1264" y2="606"/>
    <line class="branch" x1="1125" y1="637" x2="1245" y2="664"/>
    <line class="branch" x1="1125" y1="637" x2="1044" y2="707"/>
    <line class="branch" x1="1125" y1="637" x2="1149" y2="720"/>

    <line class="branch" x1="1041" y1="893" x2="1041" y2="799"/>
    <line class="branch" x1="1041" y1="893" x2="1163" y2="841"/>
    <line class="branch" x1="1041" y1="893" x2="932" y2="939"/>
    <line class="branch" x1="1041" y1="893" x2="1206" y2="923"/>
    <line class="branch" x1="1041" y1="893" x2="1142" y2="977"/>
    <line class="branch" x1="1041" y1="893" x2="1016" y2="984"/>
    <line class="branch" x1="1041" y1="893" x2="1094" y2="1031"/>

    <line class="branch" x1="435" y1="922" x2="453" y2="802"/>
    <line class="branch" x1="435" y1="922" x2="327" y2="837"/>
    <line class="branch" x1="435" y1="922" x2="311" y2="925"/>
    <line class="branch" x1="435" y1="922" x2="379" y2="1010"/>
    <line class="branch" x1="435" y1="922" x2="495" y2="1046"/>

    <line class="branch" x1="758" y1="1017" x2="706" y2="922"/>
    <line class="branch" x1="758" y1="1017" x2="613" y2="941"/>
    <line class="branch" x1="758" y1="1017" x2="899" y2="1039"/>
    <line class="branch" x1="758" y1="1017" x2="636" y2="1069"/>
    <line class="branch" x1="758" y1="1017" x2="700" y2="1159"/>
    <line class="branch" x1="758" y1="1017" x2="829" y2="1154"/>
  </g>

  <!-- leaves: event attraction / sales -->
  <g class="cluster cluster-attraction">
    <g transform="translate(760 230)"><ellipse class="tone-light" rx="32" ry="18"/><text class="leaf-label" y="3.5">COMMUNITY</text></g>
    <g transform="translate(681 268)"><ellipse class="tone-dark" rx="35" ry="20"/><text class="leaf-label" y="3.5">ENTERTAINMENT</text></g>
    <g transform="translate(838 267)"><ellipse class="tone-mid" rx="35" ry="22"/><text class="leaf-label" y="3.5">EDUCATION</text></g>
    <g transform="translate(609 324)"><ellipse class="tone-light" rx="37" ry="22"/><text class="leaf-label" y="-2">TECHNICAL</text><text class="leaf-label" y="9">SERVICES</text></g>
    <g transform="translate(848 330)"><ellipse class="tone-pale" rx="24" ry="14"/><text class="leaf-label" y="3.5">LIFESTYLE</text></g>
    <g transform="translate(676 453)"><ellipse class="tone-dark" rx="20" ry="12"/><text class="leaf-label" y="3.5">SPORT</text></g>
  </g>

  <!-- leaves: event planning management -->
  <g class="cluster cluster-planning">
    <g transform="translate(974 330)"><ellipse class="tone-dark" rx="34" ry="21"/><text class="leaf-label" y="3.5">PROCUREMENT</text></g>
    <g transform="translate(1054 353)"><ellipse class="tone-light" rx="31" ry="19"/><text class="leaf-label" y="-2">EVENT</text><text class="leaf-label" y="9">LOGISTICS</text></g>
    <g transform="translate(911 384)"><ellipse class="tone-mid" rx="31" ry="19"/><text class="leaf-label" y="-2">CLIENT</text><text class="leaf-label" y="9">ENGAGEMENT</text></g>
    <g transform="translate(849 415)"><ellipse class="tone-light" rx="23" ry="13"/><text class="leaf-label" y="3.5">BUSINESS</text></g>
    <g transform="translate(1072 414)"><ellipse class="tone-light" rx="33" ry="20"/><text class="leaf-label" y="3.5">RESOURCING</text></g>
    <g transform="translate(848 465)"><ellipse class="tone-mid" rx="32" ry="20"/><text class="leaf-label" y="-2">HEALTH</text><text class="leaf-label" y="9">AND SAFETY</text></g>
    <g transform="translate(1047 490)"><ellipse class="tone-mid" rx="30" ry="19"/><text class="leaf-label" y="-2">RETAIL</text><text class="leaf-label" y="9">MENU DESIGN</text></g>
    <g transform="translate(852 530)"><ellipse class="tone-mid" rx="36" ry="22"/><text class="leaf-label" y="-2">CORPORATE</text><text class="leaf-label" y="9">MENU DESIGN</text></g>
  </g>

  <!-- leaves: commercial -->
  <g class="cluster cluster-commercial">
    <g transform="translate(498 359)"><ellipse class="tone-mid" rx="32" ry="19"/><text class="leaf-label" y="3.5">SPONSORSHIP</text></g>
    <g transform="translate(411 403)"><ellipse class="tone-dark" rx="40" ry="25"/><text class="leaf-label" y="-2">COMMERCIAL</text><text class="leaf-label" y="9">PARTNERSHIPS</text></g>
    <g transform="translate(582 418)"><ellipse class="tone-mid" rx="31" ry="19"/><text class="leaf-label" y="-2">REVENUE</text><text class="leaf-label" y="9">GROWTH</text></g>
    <g transform="translate(407 491)"><ellipse class="tone-mid" rx="32" ry="19"/><text class="leaf-label" y="3.5">MEMBERSHIP</text></g>
    <g transform="translate(516 579)"><ellipse class="tone-light" rx="25" ry="15"/><text class="leaf-label" y="3.5">TICKETING</text></g>
  </g>

  <!-- leaves: marketing and communication -->
  <g class="cluster cluster-marketing">
    <g transform="translate(316 581)"><ellipse class="tone-mid" rx="35" ry="21"/><text class="leaf-label" y="3.5">REPUTATION</text></g>
    <g transform="translate(427 574)"><ellipse class="tone-mid" rx="22" ry="14"/><text class="leaf-label" y="3.5">BRAND</text></g>
    <g transform="translate(296 708) rotate(-25)"><ellipse class="tone-dark" rx="40" ry="25"/><text class="leaf-label" y="-2">PUBLIC</text><text class="leaf-label" y="9">RELATIONS</text></g>
    <g transform="translate(451 718)"><ellipse class="tone-dark" rx="24" ry="14"/><text class="leaf-label" y="3.5">WHAT?</text></g>
  </g>

  <!-- leaves: event delivery / operations -->
  <g class="cluster cluster-delivery">
    <g transform="translate(1064 565) rotate(15)"><ellipse class="tone-light" rx="24" ry="15"/><text class="leaf-label" y="3.5">HOSTING</text></g>
    <g transform="translate(1202 490)"><ellipse class="tone-mid" rx="40" ry="25"/><text class="leaf-label" y="-7.5">CORPORATE</text><text class="leaf-label" y="3.5">FOOD AND</text><text class="leaf-label" y="14.5">BEVERAGE</text></g>
    <g transform="translate(1221 563)"><ellipse class="tone-dark" rx="35" ry="22"/><text class="leaf-label" y="-7.5">RETAIL</text><text class="leaf-label" y="3.5">FOOD AND</text><text class="leaf-label" y="14.5">BEVERAGE</text></g>
    <g transform="translate(1008 605)"><ellipse class="tone-dark" rx="36" ry="22"/><text class="leaf-label" y="-2">EMERGENCY</text><text class="leaf-label" y="9">MANAGEMENT</text></g>
    <g transform="translate(1264 606)"><ellipse class="tone-mid" rx="33" ry="20"/><text class="leaf-label" y="-2">KITCHEN</text><text class="leaf-label" y="9">OPERATORS</text></g>
    <g transform="translate(1245 664)"><ellipse class="tone-dark" rx="37" ry="22"/><text class="leaf-label" y="-2">VENUE</text><text class="leaf-label" y="9">MANAGEMENT</text></g>
    <g transform="translate(1044 707)"><ellipse class="tone-dark" rx="27" ry="16"/><text class="leaf-label" y="3.5">CLEANING</text></g>
    <g transform="translate(1149 720)"><ellipse class="tone-mid" rx="47" ry="28"/><text class="leaf-label" y="-7.5">TRAFFIC</text><text class="leaf-label" y="3.5">MANAGEMENT AND</text><text class="leaf-label" y="14.5">CAR SERVICING</text></g>
  </g>

  <!-- leaves: system policies procedures -->
  <g class="cluster cluster-systems">
    <g transform="translate(1041 799)"><ellipse class="tone-mid" rx="44" ry="27"/><text class="leaf-label" y="-2">FINANCIAL</text><text class="leaf-label" y="9">PLANNING</text></g>
    <g transform="translate(1163 841)"><ellipse class="tone-dark" rx="47" ry="28"/><text class="leaf-label" y="-2">STATUTORY</text><text class="leaf-label" y="9">COMPLIANCE</text></g>
    <g transform="translate(932 939)"><ellipse class="tone-dark" rx="37" ry="22"/><text class="leaf-label" y="3.5">PROCEDURES</text></g>
    <g transform="translate(1206 923)"><ellipse class="tone-mid" rx="37" ry="22"/><text class="leaf-label" y="4" style="font-size:12px">POLICIES</text></g>
    <g transform="translate(1142 977)"><ellipse class="tone-dark" rx="27" ry="16"/><text class="leaf-label" y="3.5">PAYROLL</text></g>
    <g transform="translate(1016 984)"><ellipse class="tone-light" rx="24" ry="15"/><text class="leaf-label" y="4.5" style="font-size:13px">ICT</text></g>
    <g transform="translate(1094 1031)"><ellipse class="tone-dark" rx="44" ry="28"/><text class="leaf-label" y="-7.5">ACCOUNTS</text><text class="leaf-label" y="3.5">PAYABLE/</text><text class="leaf-label" y="14.5">RECEIVABLE</text></g>
  </g>

  <!-- leaves: assets and facilities management -->
  <g class="cluster cluster-assets">
    <g transform="translate(453 802)"><ellipse class="tone-light" rx="36" ry="22"/><text class="leaf-label" y="-2">REACTIVE</text><text class="leaf-label" y="9">MAINTENANCE</text></g>
    <g transform="translate(327 837)"><ellipse class="tone-dark" rx="37" ry="22"/><text class="leaf-label" y="-2">PREVENTIVE</text><text class="leaf-label" y="9">MAINTENANCE</text></g>
    <g transform="translate(311 925)"><ellipse class="tone-mid" rx="33" ry="20"/><text class="leaf-label" y="-2">CAPITAL</text><text class="leaf-label" y="9">PROGRAMME</text></g>
    <g transform="translate(379 1010)"><ellipse class="tone-dark" rx="34" ry="21"/><text class="leaf-label" y="-2">VENUE</text><text class="leaf-label" y="9">PRESENTATION</text></g>
    <g transform="translate(495 1046)"><ellipse class="tone-light" rx="36" ry="22"/><text class="leaf-label" y="-2">EVENT OKAY</text><text class="leaf-label" y="9">RESPONSE</text></g>
  </g>

  <!-- leaves: people and culture -->
  <g class="cluster cluster-people">
    <g transform="translate(706 922)"><ellipse class="tone-light" rx="30" ry="18"/><text class="leaf-label" y="3.5">CULTURE</text></g>
    <g transform="translate(613 941)"><ellipse class="tone-dark" rx="37" ry="22"/><text class="leaf-label" y="-2">CAPABILITY</text><text class="leaf-label" y="9">DEVELOPMENT</text></g>
    <g transform="translate(899 1039)"><ellipse class="tone-light" rx="48" ry="28"/><text class="leaf-label" y="-2" style="font-size:11px">RECRUITMENT</text><text class="leaf-label" y="11" style="font-size:11px">AND RETENTION</text></g>
    <g transform="translate(636 1069)"><ellipse class="tone-dark" rx="31" ry="19"/><text class="leaf-label" y="3.5">ROSTERING</text></g>
    <g transform="translate(700 1159)"><ellipse class="tone-dark" rx="57" ry="34"/><text class="leaf-label" y="-3" style="font-size:12px">COMMUNICATION</text><text class="leaf-label" y="12" style="font-size:12px">AND ENGAGEMENT</text></g>
    <g transform="translate(829 1154)"><ellipse class="tone-mid" rx="32" ry="19"/><text class="leaf-label" y="3.5">WELLBEING</text></g>
  </g>

  <!-- hubs -->
  <g class="hubs">
    <g transform="translate(759 355)"><circle class="hub-disc" r="49"/><circle class="hub-ring" r="43"/><text class="hub-label" y="-10">EVENT</text><text class="hub-label" y="4.5">ATTRACTION/</text><text class="hub-label" y="19">SALES</text></g>
    <g transform="translate(968 453)"><circle class="hub-disc" r="45"/><circle class="hub-ring" r="39"/><text class="hub-label" y="-10">EVENT</text><text class="hub-label" y="4.5">PLANNING</text><text class="hub-label" y="19">MANAGEMENT</text></g>
    <g transform="translate(509 470)"><circle class="hub-disc" r="43"/><circle class="hub-ring" r="37"/><text class="hub-label" y="4.5">COMMERCIAL</text></g>
    <g transform="translate(386 650)"><circle class="hub-disc" r="44"/><circle class="hub-ring" r="38"/><text class="hub-label" y="-8" style="font-size:10px">MARKETING</text><text class="hub-label" y="4" style="font-size:10px">AND</text><text class="hub-label" y="16" style="font-size:10px">COMMUNICATION</text></g>
    <g transform="translate(1125 637)"><circle class="hub-disc" r="43"/><circle class="hub-ring" r="37"/><text class="hub-label" y="-10">EVENT</text><text class="hub-label" y="4.5">DELIVERY/</text><text class="hub-label" y="19">OPERATIONS</text></g>
    <g transform="translate(1041 893)"><circle class="hub-disc" r="47"/><circle class="hub-ring" r="41"/><text class="hub-label" y="-10">SYSTEM</text><text class="hub-label" y="4.5">POLICIES</text><text class="hub-label" y="19">PROCEDURES</text></g>
    <g transform="translate(435 922)"><circle class="hub-disc" r="54"/><circle class="hub-ring" r="48"/><text class="hub-label" y="-10">ASSESTS AND</text><text class="hub-label" y="4.5">FACILITIES</text><text class="hub-label" y="19">MANAGEMENT</text></g>
    <g transform="translate(758 1017)"><circle class="hub-disc" r="48"/><circle class="hub-ring" r="42"/><text class="hub-label" y="-3">PEOPLE AND</text><text class="hub-label" y="12">CULTURE</text></g>
  </g>

  <!-- core -->
  <g class="core">
    <circle class="core-outer" cx="760" cy="730" r="125"/>
    <circle class="core-inner" cx="760" cy="730" r="97"/>
    <text class="phase"><textPath href="#core-cw" startOffset="8.2%">ATTRACT</textPath></text>
    <text class="phase"><textPath href="#core-cw" startOffset="24.4%">PLAN</textPath></text>
    <text class="phase"><textPath href="#core-cw" startOffset="39.2%">DELIVER</textPath></text>
    <text class="phase"><textPath href="#core-ccw" startOffset="9.2%">PREPARE</textPath></text>
    <text class="phase"><textPath href="#core-ccw" startOffset="25%">ENABLE</textPath></text>
    <text class="phase"><textPath href="#core-ccw" startOffset="41.4%">PROTECT</textPath></text>
    <text class="phase-arrow"><textPath href="#core-cw" startOffset="17.2%">›</textPath></text>
    <text class="phase-arrow"><textPath href="#core-cw" startOffset="30.4%">›</textPath></text>
    <text class="phase-arrow"><textPath href="#core-cw" startOffset="48.6%">›</textPath></text>
    <text class="phase-arrow"><textPath href="#core-ccw" startOffset="33.4%">‹</textPath></text>
    <text class="phase-arrow"><textPath href="#core-ccw" startOffset="17%">‹</textPath></text>
    <text class="phase-arrow"><textPath href="#core-ccw" startOffset="0.8%">‹</textPath></text>

    <text class="core-title" x="760" y="717">EVENTS</text>
    <line class="core-rule" x1="670" y1="741" x2="850" y2="741"/>
    <line class="core-rule" x1="668" y1="766" x2="852" y2="766"/>
    <line class="core-rule" x1="730" y1="741" x2="730" y2="823"/>
    <line class="core-rule" x1="790" y1="741" x2="790" y2="823"/>
    <text class="core-cell" x="700" y="760">VENUES</text>
    <text class="core-cell" x="760" y="760">PEOPLE</text>
    <text class="core-cell" x="819" y="760">SYSTEMS</text>
  </g>

  <!-- company name -->
  <g class="brand">
    <text class="brand-name" x="1291" y="1377">MERIDIAN</text>
    <text class="brand-name" x="1291" y="1421">VENUES</text>
  </g>
</svg>
</body>
</html>
```